Irrigation Business needs their business cards modernised and revamped

I would like to keep my current logo, colours and revamp the format of the card.

I would like the card to be clean yet important.

Im not sure if you include texture but i would like the named logo to be indented into the card etc.

show me something alive and free something thats clinical to the point yet has a feel of achievement. i would like people to go nice card.

Target Market(s)

high end clients, corporate, sports field manger, the guys that make the decisions

Industry/Entity Type

Business

Contact Information for Business Card

nformation to be included

Dorian Hesk (Director)
0487253916
dorian@tfcraft.biz
www.taddsfieldcrafts.com

instagram logo
google logo
facebook logo

Colors

Designer to choose colors to be used in the design.

Requirements
Nice to have
• indentations a really nice feel to the card good texture

```html
<!DOCTYPE html>
<html lang="en">
<head>
<meta charset="utf-8">
<title>Tadd's Field Crafts – Business Card</title>
<link href="https://fonts.googleapis.com/css2?family=Lato:wght@400;700&display=swap" rel="stylesheet">
<style>
  :root {
    --backdrop: #2b2b2b;
    --card-white: #ececec;
    --card-blue: #3a6fb6;
    --card-blue-deep: #2f5f9f;
    --brand-blue: #2d64a8;
    --brand-teal: #3a93b5;
    --brand-green: #2e9a52;
    --ink: #333840;
    --faint-dark: rgba(20,40,80,0.12);
    --faint-blue: rgba(20,40,80,0.14);
    --debossed: #1d2f4c;
  }
  * { margin: 0; padding: 0; box-sizing: border-box; }
  html, body { width: 1200px; height: 600px; overflow: hidden; }
  body {
    background: var(--backdrop);
    font-family: "Lato", sans-serif;
    position: relative;
  }
  .card {
    position: absolute;
    top: 150px;
    width: 520px;
    height: 300px;
    border-radius: 20px;
    overflow: hidden;
  }
  .card--front { left: 50px; background: var(--card-white); }
  .card--back { left: 630px; background: var(--card-blue); }

  .decor-ring { position: absolute; }
  .card--front .decor-ring { right: -90px; top: 0; }
  .card--back .decor-ring { left: -180px; top: -20px; }

  .person { position: absolute; left: 20px; top: 18px; padding-left: 16px; height: 48px; }
  .person::before {
    content: ""; position: absolute; left: 0; top: 0;
    width: 11px; height: 48px; background: var(--brand-teal);
  }
  .person__name { font-size: 23px; color: var(--ink); line-height: 28px; }
  .person__role { font-size: 13px; color: var(--brand-green); line-height: 16px; }

  .brand { position: absolute; text-align: center; white-space: nowrap; }
  .brand__mark { display: block; margin: 0 auto; border-radius: 50%; }
  .brand__name { font-weight: 700; color: var(--brand-blue); line-height: 1.15; }

  .card--front .brand { right: 14px; top: 18px; width: 190px; }
  .card--front .brand__mark {
    width: 64px; height: 64px; background: var(--brand-teal);
    border: 4px solid var(--brand-blue); margin-bottom: 10px;
  }
  .card--front .brand__name { font-size: 17px; letter-spacing: 0.3px; }

  .card--back .brand { left: 0; right: 0; top: 57px; }
  .card--back .brand__mark {
    width: 116px; height: 116px; background: var(--card-blue-deep);
    border: 5px solid var(--debossed); margin-bottom: 22px;
  }
  .card--back .brand__name { color: var(--debossed); font-size: 33px; letter-spacing: 1px; }

  .contact { position: absolute; left: 20px; top: 208px; list-style: none; }
  .contact__item {
    display: flex; align-items: center; gap: 8px;
    font-size: 14px; line-height: 18px; color: var(--ink); margin-bottom: 8px;
  }
  .contact__item svg { width: 15px; height: 13px; }

  .rule {
    position: absolute; left: 0; top: 264px; width: 390px; height: 3px;
    background: var(--brand-teal);
  }
  .web {
    position: absolute; left: 20px; top: 272px;
    font-size: 14px; line-height: 18px; color: var(--brand-blue);
  }
  .social { position: absolute; right: 28px; top: 258px; display: flex; gap: 20px; }
  .social__dot { width: 16px; height: 16px; background: var(--brand-blue); border-radius: 2px; }
</style>
</head>
<body>

<section class="card card--front">
  <svg class="decor-ring" width="300" height="300" viewBox="0 0 300 300" aria-hidden="true">
    <circle cx="150" cy="150" r="135" fill="none" stroke="var(--faint-dark)" stroke-width="14"/>
  </svg>

  <div class="person">
    <div class="person__name">Dorian Hesk</div>
    <div class="person__role">Director</div>
  </div>

  <div class="brand">
    <span class="brand__mark"></span>
    <div class="brand__name">TADD'S FIELD CRAFTS</div>
  </div>

  <ul class="contact">
    <li class="contact__item">
      <svg viewBox="0 0 15 13" aria-hidden="true"><path d="M1 4 Q7.5 -1 14 4 L12 6 L10 4.5 L5 4.5 L3 6 Z M3 7 H12 V12 H3 Z" fill="var(--brand-green)"/></svg>
      0487253916
    </li>
    <li class="contact__item">
      <svg viewBox="0 0 15 13" aria-hidden="true"><rect x="1" y="2" width="13" height="9" fill="var(--brand-green)"/><path d="M1 2 L7.5 7 L14 2" fill="none" stroke="var(--card-white)" stroke-width="1.2"/></svg>
      dorian@tfcraft.biz
    </li>
  </ul>

  <div class="rule"></div>
  <div class="web">www.taddsfieldcrafts.com</div>
  <div class="social">
    <span class="social__dot"></span>
    <span class="social__dot"></span>
    <span class="social__dot"></span>
  </div>
</section>

<section class="card card--back">
  <svg class="decor-ring" width="340" height="340" viewBox="0 0 340 340" aria-hidden="true">
    <circle cx="170" cy="170" r="155" fill="none" stroke="var(--faint-blue)" stroke-width="16"/>
  </svg>
  <div class="brand">
    <span class="brand__mark"></span>
    <div class="brand__name">TADD'S FIELD CRAFTS</div>
  </div>
</section>

</body>
</html>
```